Technology Charity needs a Web Design

Vendra Lum purchases used company mobiles and donates the proceeds to charity. It is showing companies how they can do social good, with unused technology. We would like to see designs with relevant images of social good. Open to ideas, and more is explained in the attached brief. Logo is attached as well.

```html
<!DOCTYPE html>
<html lang="en">
<head>
<meta charset="utf-8">
<title>Vendra Lum — Contact</title>
<link rel="stylesheet" href="https://fonts.googleapis.com/css2?family=Abril+Fatface&family=Mulish:wght@400;600&display=swap">
<style>
:root{
  --sage:#8fb0b8;
  --sage-dark:#7fa2ab;
  --ink:#1f2540;
  --white:#ffffff;
  --accent:#f2552c;
  --soft:#f4f4f4;
  --muted:#5c6a86;
  --hero-a:#2a2320;
  --hero-b:#4a3a33;
  --map-land:#dfe7d3;
  --map-water:#a7cdec;
}
*{box-sizing:border-box;margin:0;padding:0}
html,body{width:685px;height:1200px;overflow:hidden;background:var(--white)}
body{position:relative;font-family:'Mulish',sans-serif;color:var(--ink)}
.abs{position:absolute}
.display{font-family:'Abril Fatface',serif;font-weight:400}

/* top bar */
.topbar{top:0;left:0;width:685px;height:30px}
.topbar .note{left:187px;top:10px;font-size:8.5px;color:var(--ink)}
.topbar .note span{color:var(--sage-dark)}
.topbar .follow{left:547px;top:10px;font-size:8.5px}
.social{top:12px;width:7px;height:7px;border-radius:50%;background:var(--ink)}

/* nav */
.nav{top:30px;left:0;width:685px;height:51px;background:var(--sage)}
.brand-box{top:30px;left:56px;width:115px;height:51px;background:var(--white)}
.brand{display:flex;align-items:center;gap:5px}
.brand .dot{width:8px;height:8px;border-radius:50%;background:var(--sage)}
.brand .name{font-size:12px;font-weight:600;color:var(--sage-dark)}
.nav-item{top:45px;color:var(--white)}
.nav-item small{display:block;font-size:6px;margin-bottom:3px}
.nav-item b{font-weight:400;font-size:9px;white-space:nowrap}
.search{top:46px;left:625px;width:18px;height:18px;border:1px solid #9b8fd6;border-radius:50%}

/* hero */
.hero{top:81px;left:0;width:685px;height:228px;background:radial-gradient(ellipse at 55% 45%,var(--hero-b),var(--hero-a) 70%)}
.hero h1{position:absolute;width:100%;top:80px;text-align:center;font-size:24px;color:var(--white)}
.crumbs{position:absolute;width:100%;top:116px;text-align:center;font-size:9.5px;color:var(--white)}
.crumbs i{display:inline-block;width:3px;height:3px;border-radius:50%;background:var(--accent);margin:0 5px 2px}

/* quick contact */
.quick{top:364px;left:24px;width:258px;height:241px;background:var(--sage);color:var(--white);padding:22px 22px}
.quick h2{font-size:19px;margin-bottom:18px}
.qrow{display:flex;align-items:center;gap:6px;font-size:10.5px;margin-bottom:8px}
.qtext{font-size:10.5px;line-height:18px;margin-bottom:11px}

/* form */
.form{top:364px;left:309px;width:347px;height:245px;border:1px dotted #8aa0c6;padding:14px 15px}
.form h3{font-size:12px;color:var(--ink)}
.form p{font-size:7.5px;color:var(--muted);margin-top:8px}
.field{background:var(--soft);font-size:7.5px;color:var(--muted);padding:0 6px;display:flex;align-items:center}
.btn{top:570px;left:323px;width:79px;height:25px;border-radius:13px;background:var(--sage);color:var(--white);font-size:7.5px;display:flex;align-items:center;justify-content:center;gap:4px}

/* map */
.map{top:662px;left:0;width:685px;height:268px;background:linear-gradient(100deg,var(--map-land) 0%,var(--map-land) 48%,var(--map-water) 60%,var(--map-water) 100%)}

/* footer */
.footer{top:930px;left:0;width:685px;height:228px;background:var(--sage);color:var(--white)}
.fhead{top:55px;font-size:11px}
.flist{top:80px;font-size:8.5px;line-height:17.4px}
.fsmall{font-size:7.5px}
.thumb{width:44px;height:36px;border-radius:2px}
.news{font-size:8.5px;line-height:13px}
.news .meta{font-size:8px;margin-top:3px}
.news .meta i{display:inline-block;width:4px;height:4px;border-radius:50%;background:var(--accent);margin-right:3px}

/* bottom */
.bottom{top:1158px;left:0;width:685px;height:42px}
.bottom .copy{left:263px;top:14px;font-size:9px;color:var(--sage-dark)}
.bottom .legal{left:503px;top:14px;font-size:9px;color:var(--sage-dark)}
</style>
</head>
<body>

<header class="abs topbar">
  <div class="abs note">The fund will go to the poor... <span>Donate Now</span></div>
  <div class="abs follow">Follow us:</div>
  <div class="abs social" style="left:594px"></div>
  <div class="abs social" style="left:608px"></div>
  <div class="abs social" style="left:622px"></div>
  <div class="abs social" style="left:636px"></div>
</header>

<nav class="abs nav" aria-label="Main">
  <div class="abs nav-item" style="left:187px;top:15px"><small>01</small><b>What We Do ⌄</b></div>
  <div class="abs nav-item" style="left:261px;top:15px"><small>02</small><b>Benefits</b></div>
  <div class="abs nav-item" style="left:309px;top:15px"><small>03</small><b>How Does It Work? ⌄</b></div>
  <div class="abs nav-item" style="left:406px;top:15px"><small>04</small><b>Contact Us ⌄</b></div>
  <div class="abs nav-item" style="left:470px;top:15px"><small>05</small><b>Our Mission ⌄</b></div>
  <div class="abs nav-item" style="left:537px;top:15px"><small>06</small><b>Contact</b></div>
  <div class="abs search" style="top:16px">
    <svg width="16" height="16" viewBox="0 0 16 16"><circle cx="7.5" cy="7.5" r="2.5" fill="none" stroke="#fff" stroke-width="1"/><line x1="9.3" y1="9.3" x2="11" y2="11" stroke="#fff" stroke-width="1"/></svg>
  </div>
</nav>
<div class="abs brand-box">
  <div class="abs brand" style="left:16px;top:20px"><span class="dot"></span><span class="name">Vendra Lum</span></div>
</div>

<section class="abs hero" role="img" aria-label="Close-up photograph of a child looking up at the camera">
  <h1 class="display">Contact</h1>
  <div class="crumbs">Home<i></i>Contact</div>
</section>

<aside class="abs quick">
  <h2 class="display">Quick Contact</h2>
  <div class="qrow">
    <svg width="9" height="12" viewBox="0 0 9 12"><path d="M4.5 0C2 0 0 2 0 4.4 0 7.6 4.5 12 4.5 12S9 7.6 9 4.4C9 2 7 0 4.5 0z" fill="#f4a27c"/><circle cx="4.5" cy="4.4" r="1.6" fill="#8fb0b8"/></svg>
    <span style="margin-left:6px">LOCATION</span></div>
  <div class="qtext">48 Marrow Lane, Estelby<br>Harbour, Nordvale</div>
  <div class="qrow">
    <svg width="12" height="12" viewBox="0 0 12 12"><path d="M2 1l2 0 1 3-1.5 1a7 7 0 0 0 3.5 3.5L8 7l3 1v2c0 .6-.4 1-1 1C5 11 1 7 1 2c0-.6.4-1 1-1z" fill="none" stroke="#f4a27c" stroke-width="1"/></svg>
    <span style="margin-left:6px">CALL US</span></div>
  <div class="qtext">555-0142-0198</div>
  <div class="qrow">
    <svg width="12" height="9" viewBox="0 0 12 9"><rect width="12" height="9" fill="#f4a27c"/><path d="M0 0l6 5 6-5" fill="none" stroke="#fff" stroke-width="1"/></svg>
    <span style="margin-left:6px">EMAIL US</span></div>
  <div class="qtext">support@vendralum.org</div>
</aside>

<section class="abs form">
  <h3 class="display">Let’s Talk!</h3>
  <p>Complete the form below and Vendra Lum will contact you.</p>
</section>
<div class="abs field" style="left:324px;top:427px;width:150px;height:26px">Name</div>
<div class="abs field" style="left:490px;top:427px;width:150px;height:26px">Phone</div>
<div class="abs field" style="left:324px;top:462px;width:150px;height:26px">email</div>
<div class="abs field" style="left:490px;top:462px;width:150px;height:26px">Website</div>
<div class="abs field" style="left:324px;top:497px;width:316px;height:55px;align-items:flex-start;padding-top:9px">Write Something</div>
<div class="abs btn">Contact Us
  <svg width="8" height="6" viewBox="0 0 8 6"><path d="M0 3h7M5 1l2 2-2 2" fill="none" stroke="#fff" stroke-width=".8"/></svg></div>

<section class="abs map" role="img" aria-label="Street map of the city and surrounding coastline"></section>

<footer class="abs footer">
  <h4 class="abs fhead display" style="left:41px">Contact Info</h4>
  <h4 class="abs fhead display" style="left:196px">Our Support</h4>
  <h4 class="abs fhead display" style="left:351px">Our Services</h4>
  <h4 class="abs fhead display" style="left:454px">Recent News</h4>

  <div class="abs fsmall" style="left:41px;top:80px;line-height:13px">
    <div style="display:flex;align-items:center;gap:5px"><svg width="7" height="9" viewBox="0 0 9 12"><path d="M4.5 0C2 0 0 2 0 4.4 0 7.6 4.5 12 4.5 12S9 7.6 9 4.4C9 2 7 0 4.5 0z" fill="#f2552c"/></svg>LOCATION</div>
    <div style="margin-top:5px">48 Marrow Lane, Estelby<br>Harbour, Nordvale</div>
    <div style="display:flex;align-items:center;gap:5px;margin-top:8px"><svg width="9" height="9" viewBox="0 0 12 12"><path d="M2 1l2 0 1 3-1.5 1a7 7 0 0 0 3.5 3.5L8 7l3 1v2c0 .6-.4 1-1 1C5 11 1 7 1 2c0-.6.4-1 1-1z" fill="none" stroke="#f2552c" stroke-width="1.2"/></svg>CALL US</div>
    <div style="margin-top:5px">555-0142-0198</div>
    <div style="display:flex;align-items:center;gap:5px;margin-top:8px"><svg width="9" height="7" viewBox="0 0 12 9"><rect width="12" height="9" fill="#f2552c"/><path d="M0 0l6 5 6-5" fill="none" stroke="#fff"/></svg>EMAIL US</div>
    <div style="margin-top:5px">hello@kelvane.org</div>
  </div>

  <div class="abs flist" style="left:196px">Private Policies<br>Donate Now<br>Become A Volunteer<br>Careers<br>Contact Us<br>Paid Programs<br>Partnership</div>
  <div class="abs flist" style="left:351px">Donate<br>Sponsor<br>Fundraise<br>Volunteer<br>Partner<br>Jobs<br>Form</div>

  <div class="abs thumb" style="left:454px;top:82px;background:linear-gradient(135deg,#c99a54,#8a4a3c)" role="img" aria-label="Photo of a child sitting outdoors"></div>
  <div class="abs" style="left:509px;top:83px;width:1px;height:40px;border-left:1px dashed #fff"></div>
  <div class="abs news" style="left:520px;top:82px">Support About Poverty To<br>Poor Family<div class="meta"><i></i>Poor, 22 January</div></div>

  <div class="abs thumb" style="left:454px;top:140px;background:linear-gradient(135deg,#6b4a3a,#3e7b93)" role="img" aria-label="Photo of a young boy"></div>
  <div class="abs" style="left:509px;top:141px;width:1px;height:40px;border-left:1px dashed #fff"></div>
  <div class="abs news" style="left:520px;top:140px">Mostly Suffered School Boys<br>Care<div class="meta"><i></i>Health, 24 February</div></div>
</footer>

<div class="abs bottom">
  <div class="abs brand" style="left:42px;top:12px"><span class="dot"></span><span class="name">Vendra Lum</span></div>
  <div class="abs copy">2020 Vendra Lum . All Rights Reserved</div>
  <div class="abs legal">Terms &amp; Conditions Privacy Policy</div>
</div>

</body>
</html>
```